I am medical doctor in surgery specialized in Urology and anti-aging. I need Web and Snapfolio design for a head cream , face cream and body lotion. I did a 2% GHK-Cu solution (head-face-body) with an professional pharmacist specialized in manufacturing creams. . GHK-Cu is a tri-peptide with solid scientific background to rejuvenate the skin (will stimulate collagen production) and can promote hair regrowth. Statistically 70% of peptides bought are fake on the market, I can personally guarantee about purity (my peptides are certified pure above 99% checked in an independent laboratory in London -UK.
I want to use the name 'Lunavel'. I secured already the domain names. I had an design for another project I could re-use for this project. The ribbon should include more blue. The font of Lunavel can be changed. I got a logo which is ok for me. Web design best coded with Wordpress.

Target Market(s)

Anti aging, skin care, hair regrowth, skin collagen

Industry/Entity Type

the cream can also be used after surgery for faster and better wound healing

Number of Pages Required

5+ page

Font styles to use
Sans Serif

Colors
0054AA
0677BA
7BADD7
CADEEF
E8F1F8

Requirements
Must have
• target population 30-70 years
Nice to have
• scientific proof, pictures before-after
Should not have
• GHK-Cu has solid scientific animal studies of anti-cancer properties. It is 100% safe for dermal human use.

```html
<!DOCTYPE html>
<html lang="en">
<head>
<meta charset="utf-8">
<title>Lunavel — Real Results</title>
<link rel="stylesheet" href="https://fonts.googleapis.com/css2?family=Montserrat:wght@500;600;700&family=Carlito:wght@400;700&display=swap">
<style>
:root{
  --navy:#0054AA;
  --blue:#0677BA;
  --sky:#7BADD7;
  --mist:#CADEEF;
  --ice:#E8F1F8;
  --ink:#1B2A3A;
  --muted:#5f718a;
  --footer:#1B2A3A;
  --logo:#2b93cb;
  --line:#d6e3ef;
}
*{margin:0;padding:0;box-sizing:border-box}
html,body{width:812px;height:1200px;overflow:hidden;background:#fff}
body{position:relative;font-family:"Carlito",sans-serif;color:var(--ink)}
.head-font{font-family:"Montserrat",sans-serif}

.promo-bar{position:absolute;top:0;left:0;width:812px;height:25px;background:linear-gradient(90deg,var(--navy),var(--blue));color:#fff;font:600 8px/25px "Montserrat",sans-serif;text-align:center;letter-spacing:.1px}

.site-header{position:absolute;top:25px;left:0;width:812px;height:60px;border-bottom:1px solid #e3e8ee;background:#fff}
.brand{position:absolute;left:60px;top:20px;font:600 14px/1 "Montserrat",sans-serif;color:var(--logo);letter-spacing:.3px}
.main-nav{position:absolute;left:212px;top:0;height:60px;display:flex;align-items:center;gap:19.5px}
.main-nav a{font:500 8.5px/1 "Montserrat",sans-serif;letter-spacing:.8px;color:var(--ink);text-decoration:none;padding:4px 0}
.main-nav a.active{color:var(--navy);border-bottom:1.5px solid var(--navy)}
.btn{display:inline-flex;align-items:center;justify-content:center;background:var(--navy);color:#fff;font:700 8.5px/1 "Montserrat",sans-serif;letter-spacing:1px;border-radius:4px;text-decoration:none}
.shop-btn{position:absolute;left:651px;top:15px;width:102px;height:31px}

.page-hero{position:absolute;top:85px;left:0;width:812px;height:131px;background:linear-gradient(100deg,var(--ice),var(--mist));text-align:center}
.page-hero h1{font:700 25px/1 "Montserrat",sans-serif;margin-top:41px}
.page-hero p{font-size:11px;color:var(--muted);margin-top:16px}

.results{position:absolute;top:216px;left:0;width:812px;height:491px;text-align:center}
.results h2{font:700 22px/1 "Montserrat",sans-serif;margin-top:53px}
.results .lead{font-size:11px;line-height:18.5px;color:var(--muted);width:360px;margin:14px auto 0}
.cards{position:absolute;top:152px;left:60px;display:flex;gap:20px}
.card{width:217px;height:232px;border:1px solid var(--line);border-radius:6px;overflow:hidden;background:#fff}
.photo{position:relative;display:flex;height:179px}
.photo .half{flex:1;position:relative}
.photo .tag{position:absolute;left:4px;bottom:3px;font:700 9px/1 "Montserrat",sans-serif;color:#fff}
.face .b{background:linear-gradient(160deg,#c9a896,#e0c2b0)}
.face .a{background:linear-gradient(160deg,#c89a84,#e4b9a4)}
.hair .b{background:linear-gradient(160deg,#5c6068,#b5a6a0)}
.hair .a{background:linear-gradient(160deg,#34363c,#a98f86)}
.scar .b{background:linear-gradient(160deg,#c79c86,#e3bfa9)}
.scar .a{background:linear-gradient(120deg,#5b6f8a 0 25%,#dcb7a2 25%)}
.card h3{font:600 10px/1 "Montserrat",sans-serif;margin-top:14px}
.card p{font-size:7.6px;color:var(--muted);margin-top:7px}
.disclaimer{position:absolute;top:418px;left:0;width:812px;font-size:8px;line-height:14.5px;color:var(--muted)}

.share{position:absolute;top:707px;left:0;width:812px;height:230px;background:var(--ice);text-align:center}
.share h2{font:700 22px/1 "Montserrat",sans-serif;margin-top:51px}
.share p{font-size:11px;line-height:18px;color:var(--muted);width:390px;margin:14px auto 0}
.follow-btn{position:absolute;left:321px;top:151px;width:170px;height:31px}

.site-footer{position:absolute;top:937px;left:0;width:812px;height:263px;background:var(--footer);color:#c9d3df}
.site-footer .brand{top:37px}
.about-text{position:absolute;left:60px;top:87px;width:200px;font-size:8px;line-height:15.2px}
.foot-col{position:absolute;top:36px}
.foot-col h4{font:600 10px/1 "Montserrat",sans-serif;color:#fff;margin-bottom:17px}
.foot-col a{display:block;font-size:8px;color:#c9d3df;text-decoration:none;margin-bottom:12.5px}
.foot-rule{position:absolute;left:60px;top:219px;width:693px;height:1px;background:#33435a}
.legal{position:absolute;left:60px;top:237px;width:693px;display:flex;justify-content:space-between;font-size:7.6px}
.legal nav a{color:#7d8ba0;text-decoration:none;margin-left:14px}
</style>
</head>
<body>

<div class="promo-bar">Clinically proven GHK-Cu • 99%+ purity certified • Trusted by surgeons worldwide</div>

<header class="site-header">
  <div class="brand">LUNAVEL</div>
  <nav class="main-nav">
    <a href="#">HOME</a><a href="#">PRODUCTS</a><a href="#">SCIENCE</a><a href="#" class="active">RESULTS</a><a href="#">ABOUT</a><a href="#">CONTACT</a>
  </nav>
  <a href="#" class="btn shop-btn">SHOP NOW</a>
</header>

<section class="page-hero">
  <h1>Real Results</h1>
  <p>Before and after photos from real Lunavel users. Individual results may vary.</p>
</section>

<section class="results">
  <h2>Before &amp; After</h2>
  <p class="lead">Witness the visible difference GHK-Cu makes. These are real results from consistent use of Lunavel formulations.</p>
  <div class="cards">
    <article class="card">
      <div class="photo face">
        <div class="half b" role="img" aria-label="Close-up of eye area skin with wrinkles before treatment"><span class="tag">BEFORE</span></div>
        <div class="half a" role="img" aria-label="Close-up of smoother eye area skin after treatment"><span class="tag">AFTER</span></div>
      </div>
      <h3>Facial Rejuvenation</h3>
      <p>12 weeks of Lunavel Face Cream</p>
    </article>
    <article class="card">
      <div class="photo hair">
        <div class="half b" role="img" aria-label="Thinning hairline before treatment"><span class="tag">BEFORE</span></div>
        <div class="half a" role="img" aria-label="Denser hairline after treatment"><span class="tag">AFTER</span></div>
      </div>
      <h3>Hair Regrowth</h3>
      <p>16 weeks of Lunavel Head Cream</p>
    </article>
    <article class="card">
      <div class="photo scar">
        <div class="half b" role="img" aria-label="Red surgical scar on an arm before treatment"><span class="tag">BEFORE</span></div>
        <div class="half a" role="img" aria-label="Faded surgical scar on an arm after treatment"><span class="tag">AFTER</span></div>
      </div>
      <h3>Post-Surgery Healing</h3>
      <p>8 weeks of Lunavel Body Lotion</p>
    </article>
  </div>
  <p class="disclaimer">Results are based on individual experiences. Results may vary depending on skin type, age, and<br>consistency of use. For best results, use Lunavel products twice daily.</p>
</section>

<section class="share">
  <h2>Share Your Results</h2>
  <p>Join the Lunavel community. Tag us in your before and after photos for a chance to be featured.</p>
  <a href="#" class="btn follow-btn">FOLLOW ON SNAPFOLIO</a>
</section>

<footer class="site-footer">
  <div class="brand">LUNAVEL</div>
  <p class="about-text">Advanced GHK-Cu formulations developed by a board-certified surgeon. Scientifically proven to rejuvenate skin, stimulate collagen, and promote hair regrowth. Every batch independently tested for purity above 99%.</p>
  <div class="foot-col" style="left:332px">
    <h4>Quick Links</h4>
    <a href="#">Home</a><a href="#">Products</a><a href="#">About Us</a><a href="#">The Science</a><a href="#">Results</a><a href="#">Contact</a>
  </div>
  <div class="foot-col" style="left:480px">
    <h4>Products</h4>
    <a href="#">Head Cream</a><a href="#">Face Cream</a><a href="#">Body Lotion</a>
  </div>
  <div class="foot-col" style="left:628px">
    <h4>Contact</h4>
    <a href="#">info@lunavel.com</a><a href="#">Get in Touch</a><a href="#">FAQ</a>
  </div>
  <div class="foot-rule"></div>
  <div class="legal">
    <span>© 2026 Lunavel. All rights reserved.</span>
    <nav><a href="#">Privacy Policy</a><a href="#">Terms of Service</a></nav>
  </div>
</footer>

</body>
</html>
```